Lantern Method of Ascent Programme Graphic

Please refer to attached graphic.
I wish to redesign this graphic to represent a programme of work that we (Vendro) deliver to our customers.
The design represents 9 steps ( 3 steps at each of 3 levels) and is all about implementing the 'Lantern Method of Ascent'

I like the fact that the increasing business growth is evident when you are progressing through the stages, but the current graphic looks dated and the colours are not working.
I would also like to incorporate the LMA logo we have created.

Target Market(s)

IT Sector - businesses looking to grow

Industry/Entity Type

We are a digital marketing company

Requirements
Must have
• Clear, concise design
Should not have
• Design must not be complicated

```html
<!DOCTYPE html>
<html lang="en">
<head>
<meta charset="utf-8">
<title>Lantern Method of Ascent – Programme Graphic</title>
<link rel="stylesheet" href="https://fonts.googleapis.com/css2?family=Inter:wght@500;600;700;800&display=swap">
<style>
  :root {
    --bg: #0f172a;
    --bg-soft: #1e293b;
    --stage-one: #38bdf8;
    --stage-one-deep: #0e7fb3;
    --stage-two: #6366f1;
    --stage-two-deep: #4338ca;
    --stage-three: #a855f7;
    --stage-three-deep: #7e22ce;
    --white: #ffffff;
    --ink: #0f172a;
    --muted: #cbd5e1;
  }
  html, body {
    margin: 0;
    padding: 0;
    width: 1200px;
    height: 675px;
    overflow: hidden;
    background: var(--bg);
  }
  .programme {
    display: block;
    width: 1200px;
    height: 675px;
    font-family: "Inter", "Helvetica Neue", Arial, sans-serif;
  }
  .stage { stroke: var(--bg); stroke-width: 5; stroke-linejoin: round; }
  .stage-one { fill: var(--stage-one); }
  .stage-two { fill: var(--stage-two); }
  .stage-three { fill: var(--stage-three); }
  .band-one { fill: var(--stage-one-deep); }
  .band-two { fill: var(--stage-two-deep); }
  .band-three { fill: var(--stage-three-deep); }
  .badge { fill: var(--white); }
  .badge-num { font-size: 44px; font-weight: 800; text-anchor: middle; }
  .badge-num.one { fill: var(--stage-one-deep); }
  .badge-num.two { fill: var(--stage-two-deep); }
  .badge-num.three { fill: var(--stage-three-deep); }
  .stage-label { fill: var(--white); font-size: 29px; font-weight: 800; letter-spacing: 0.5px; }
  .step-box { fill: var(--white); }
  .step-text { fill: var(--ink); font-size: 19px; font-weight: 600; text-anchor: middle; }
  .step-text.lead { font-size: 22px; font-weight: 700; }
  .band-title { fill: var(--white); font-size: 21px; font-weight: 700; }
  .band-sub { fill: var(--white); font-size: 19px; font-weight: 500; opacity: 0.9; }
  .value-pill { fill: var(--stage-two); }
  .value-text { fill: var(--white); font-size: 33px; font-weight: 800; text-anchor: middle; }
  .value-head { fill: var(--stage-three); }
  .mark-box { fill: var(--white); }
  .mark-name { fill: var(--stage-two-deep); font-size: 30px; font-weight: 800; text-anchor: middle; }
</style>
</head>
<body>
<svg class="programme" viewBox="0 0 1280 720" xmlns="http://www.w3.org/2000/svg" aria-label="Lantern Method of Ascent programme: three stages rising in business value">
  <defs>
    <linearGradient id="axis-fade" x1="0" y1="1" x2="0" y2="0">
      <stop offset="0" stop-color="var(--bg-soft)"/>
      <stop offset="0.5" stop-color="var(--stage-two)"/>
      <stop offset="1" stop-color="var(--stage-three)"/>
    </linearGradient>
  </defs>

  <!-- Business value axis -->
  <g class="value-axis">
    <rect x="158" y="58" width="14" height="630" rx="7" fill="url(#axis-fade)"/>
    <path class="value-head" d="M165 18 L198 64 L132 64 Z"/>
    <rect class="value-pill" x="15" y="98" width="300" height="90" rx="45"/>
    <text class="value-text" x="165" y="155">Business Value</text>
  </g>

  <!-- Stage shapes -->
  <g class="stages">
    <path class="stage stage-one" d="M200 600 L565 268 Q595 242 625 248 Q655 256 655 292 L655 600 Z"/>
    <path class="stage stage-two" d="M655 355 L860 160 Q882 148 905 151 Q945 158 945 200 L945 600 L655 600 Z"/>
    <path class="stage stage-three" d="M945 272 L1150 84 Q1172 72 1195 76 Q1238 84 1238 130 L1238 600 L945 600 Z"/>
  </g>

  <!-- Stage badges -->
  <g class="badges">
    <rect class="badge" x="520" y="223" width="78" height="78" rx="18"/>
    <text class="badge-num one" x="559" y="278">1</text>
    <rect class="badge" x="800" y="143" width="76" height="76" rx="18"/>
    <text class="badge-num two" x="838" y="197">2</text>
    <rect class="badge" x="1085" y="60" width="76" height="76" rx="18"/>
    <text class="badge-num three" x="1123" y="114">3</text>
  </g>

  <!-- Stage labels -->
  <text class="stage-label" transform="translate(340 528) rotate(-42)">Lantern</text>
  <text class="stage-label" transform="translate(706 360) rotate(-45)">Method</text>
  <text class="stage-label" transform="translate(1000 278) rotate(-40)">Ascent</text>

  <!-- Steps -->
  <g class="steps">
    <rect class="step-box" x="478" y="387" width="139" height="56" rx="10"/>
    <text class="step-text" x="547" y="422">Personas</text>
    <rect class="step-box" x="478" y="456" width="139" height="56" rx="10"/>
    <text class="step-text" x="547" y="491">Database</text>
    <rect class="step-box" x="478" y="522" width="139" height="56" rx="10"/>
    <text class="step-text" x="547" y="557">Systems</text>

    <rect class="step-box" x="748" y="390" width="139" height="57" rx="10"/>
    <text class="step-text lead" x="817" y="426">Messaging</text>
    <rect class="step-box" x="748" y="460" width="139" height="56" rx="10"/>
    <text class="step-text" x="817" y="495">Leads</text>
    <rect class="step-box" x="748" y="526" width="139" height="56" rx="10"/>
    <text class="step-text" x="817" y="561">Pipeline</text>

    <rect class="step-box" x="1048" y="385" width="139" height="56" rx="10"/>
    <text class="step-text" x="1117" y="420">Sales</text>
    <rect class="step-box" x="1048" y="454" width="139" height="56" rx="10"/>
    <text class="step-text" x="1117" y="489">Nurture</text>
    <rect class="step-box" x="1048" y="520" width="139" height="56" rx="10"/>
    <text class="step-text" x="1117" y="555">Reference</text>
  </g>

  <!-- Review band -->
  <g class="review-band">
    <path class="band-one" d="M652 606 L652 686 L215 686 Q199 686 199 670 L199 622 Q199 606 215 606 Z"/>
    <rect class="band-two" x="658" y="606" width="284" height="80"/>
    <path class="band-three" d="M948 606 L1222 606 Q1238 606 1238 622 L1238 670 Q1238 686 1222 686 L948 686 Z"/>

    <text class="band-title" x="302" y="638">Numbers that Matter</text>
    <text class="band-sub" x="302" y="667">Foundation Metrics</text>
    <text class="band-title" x="697" y="638">Weekly Scorecard</text>
    <text class="band-sub" x="697" y="667">Tactical Execution</text>
    <text class="band-title" x="980" y="638">Monthly Scorecard</text>
    <text class="band-sub" x="980" y="667">Strategic Review</text>
  </g>

  <!-- Programme mark -->
  <g class="programme-mark">
    <rect class="mark-box" x="22" y="607" width="88" height="88" rx="14"/>
    <text class="mark-name" x="66" y="662">LMA</text>
  </g>
</svg>
</body>
</html>
```